Marlow Crest Group (Real Estate and Investment)

A high end, clean design.
We are a real estate company with sales, asset management and investment divisions. We want to use a black and white scheme which is really high end feel. The back of the card can just be the logo (black background with the white writing) as we will probably emboss this when we print)

Target Market(s)

High level investors, high end houses for sale

Industry/Entity Type

Business

Contact Information for Business Card

Name, position, phone number and email address
Glen Varley, Managing Director, 0437259064 and glen@marlowcrest-example.com.au

Requirements
Must have
• Back of the card to be the black background with the white writing (as per the attached images). Would like the capacity to emboss the writing and logo

```html
<!DOCTYPE html>
<html lang="en">
<head>
<meta charset="utf-8">
<title>Marlow Crest Group – Business Cards</title>
<link rel="stylesheet" href="https://fonts.googleapis.com/css2?family=Montserrat:wght@400;500;700&display=swap">
<style>
  :root {
    --page: #e9ecea;
    --card-black: #141112;
    --card-black-soft: #2a2628;
    --card-charcoal: #353436;
    --card-charcoal-soft: #434244;
    --accent-teal: #3a9fae;
    --text-white: #ffffff;
    --text-muted: #d9dcdc;
  }
  * { box-sizing: border-box; margin: 0; padding: 0; }
  html, body { width: 1200px; height: 947px; overflow: hidden; }
  body {
    background: var(--page);
    font-family: "Montserrat", sans-serif;
    position: relative;
  }
  .card {
    position: absolute;
    top: 312px;
    width: 456px;
    height: 254px;
    overflow: hidden;
  }
  .card--front { left: 122px; }
  .card--back { left: 636px; }
  .card__art { position: absolute; inset: 0; width: 100%; height: 100%; }

  .brand {
    position: absolute;
    display: flex;
    flex-direction: column;
    align-items: center;
    gap: 12px;
    transform: translateX(-50%);
  }
  .brand__dot {
    width: 46px; height: 46px;
    border-radius: 50%;
    border: 1.5px solid var(--text-white);
  }
  .brand__name {
    color: var(--text-white);
    font-weight: 500;
    font-size: 14px;
    letter-spacing: 0.2px;
    white-space: nowrap;
  }
  .card--front .brand { left: 162px; top: 75px; }
  .card--back .brand { left: 327px; top: 32px; }
  .card--back .brand__dot { width: 40px; height: 40px; }
  .card--back .brand__name { font-size: 13px; }

  .person { position: absolute; left: 257px; top: 139px; }
  .person__name {
    color: var(--text-white);
    font-size: 20px;
    font-weight: 400;
    line-height: 1;
    white-space: nowrap;
  }
  .person__name strong { font-weight: 700; }
  .person__role {
    color: var(--accent-teal);
    font-size: 6.5px;
    font-weight: 500;
    margin-top: 3px;
    margin-left: 2px;
  }
  .contact {
    position: absolute;
    left: 258px;
    top: 183px;
    list-style: none;
    display: flex;
    flex-direction: column;
    gap: 5px;
  }
  .contact__item {
    display: flex;
    align-items: center;
    gap: 9px;
    color: var(--text-muted);
    font-size: 9.5px;
    white-space: nowrap;
  }
  .contact__icon { width: 11px; height: 11px; flex: none; }
</style>
</head>
<body>

  <section class="card card--front" aria-label="Card front">
    <svg class="card__art" viewBox="0 0 555 308" preserveAspectRatio="none" aria-hidden="true">
      <defs>
        <linearGradient id="front-base" x1="0" y1="0" x2="1" y2="1">
          <stop offset="0" stop-color="#1c191a"/>
          <stop offset="0.55" stop-color="var(--card-black)"/>
          <stop offset="1" stop-color="#221f20"/>
        </linearGradient>
        <linearGradient id="front-house" x1="0" y1="0" x2="0" y2="1">
          <stop offset="0" stop-color="#d8cfae"/>
          <stop offset="0.45" stop-color="#7d5d45"/>
          <stop offset="0.8" stop-color="#c9c4a2"/>
          <stop offset="1" stop-color="#5e7d3a"/>
        </linearGradient>
      </defs>
      <rect width="555" height="308" fill="url(#front-base)"/>
      <polygon points="137,0 452,0 362,30" fill="var(--accent-teal)"/>
      <polygon points="342,22 365,28 512,308 472,308" fill="var(--card-charcoal)"/>
      <g role="img" aria-label="Photograph of a two-storey luxury house with stone cladding">
        <polygon points="365,28 452,0 555,0 555,308 512,308" fill="url(#front-house)"/>
      </g>
    </svg>
    <div class="brand">
      <span class="brand__dot"></span>
      <span class="brand__name">MARLOW CREST GROUP</span>
    </div>
  </section>

  <section class="card card--back" aria-label="Card back">
    <svg class="card__art" viewBox="0 0 555 308" preserveAspectRatio="none" aria-hidden="true">
      <defs>
        <linearGradient id="back-base" x1="0" y1="0" x2="1" y2="1">
          <stop offset="0" stop-color="var(--card-charcoal-soft)"/>
          <stop offset="0.6" stop-color="var(--card-charcoal)"/>
          <stop offset="1" stop-color="#2c2b2d"/>
        </linearGradient>
        <linearGradient id="back-house" x1="0" y1="0" x2="0" y2="1">
          <stop offset="0" stop-color="#2f6fc4"/>
          <stop offset="0.25" stop-color="#cbbd97"/>
          <stop offset="0.5" stop-color="#7a5a42"/>
          <stop offset="0.8" stop-color="#d2ccaa"/>
          <stop offset="1" stop-color="#607f3b"/>
        </linearGradient>
      </defs>
      <rect width="555" height="308" fill="url(#back-base)"/>
      <g role="img" aria-label="Photograph of a two-storey luxury house under a blue sky">
        <polygon points="0,0 286,0 5,308 0,308" fill="url(#back-house)"/>
      </g>
      <polygon points="286,0 300,0 80,308 5,308" fill="var(--accent-teal)"/>
    </svg>
    <div class="brand">
      <span class="brand__dot"></span>
      <span class="brand__name">MARLOW CREST GROUP</span>
    </div>
    <div class="person">
      <p class="person__name">Glen <strong>Varley</strong></p>
      <p class="person__role">Managing Director</p>
    </div>
    <ul class="contact">
      <li class="contact__item">
        <svg class="contact__icon" viewBox="0 0 24 24" aria-hidden="true">
          <path fill="var(--accent-teal)" d="M6.6 10.8a15.1 15.1 0 0 0 6.6 6.6l2.2-2.2c.3-.3.7-.4 1-.2 1.1.4 2.3.6 3.6.6.6 0 1 .4 1 1V20c0 .6-.4 1-1 1A17 17 0 0 1 3 4c0-.6.4-1 1-1h3.5c.6 0 1 .4 1 1 0 1.3.2 2.5.6 3.6.1.3 0 .7-.2 1z"/>
        </svg>
        <span>0437259064</span>
      </li>
      <li class="contact__item">
        <svg class="contact__icon" viewBox="0 0 24 24" aria-hidden="true">
          <path fill="var(--accent-teal)" d="M2 9l10-6 10 6v11a1 1 0 0 1-1 1H3a1 1 0 0 1-1-1z"/>
          <path fill="none" stroke="var(--card-charcoal)" stroke-width="1.6" d="M2.5 9.5l9.5 6 9.5-6"/>
        </svg>
        <span>glen@marlowcrest-example.com.au</span>
      </li>
    </ul>
  </section>

</body>
</html>
```